Webdesign mit Grundfarbe Weinrot für allgemeine Steuerberatung
Zielgruppe
Allgemeine Steuerberatung. Zielgruppe ist breit gefächert, allerdings soll die Webseite eher den Jungunternehmer ansprechen.
Aufgabenstellung
Die Grundfarbe sollte weinrot sein.

```html
<!DOCTYPE html>
<html lang="de">
<head>
<meta charset="utf-8">
<title>Steuerberatung Kivra</title>
<link href="https://fonts.googleapis.com/css2?family=PT+Sans:ital,wght@0,400;0,700;1,400;1,700&display=swap" rel="stylesheet">
<style>
:root{
  --wine:#6b1117;
  --wine-dark:#5a0e13;
  --mauve:#9d5c5f;
  --mauve-light:#b77b7d;
  --text:#222;
  --white:#fff;
  --frame:#c9c9c9;
}
*{margin:0;padding:0;box-sizing:border-box}
html,body{width:667px;height:1200px;overflow:hidden;background:var(--white)}
body{font-family:"PT Sans",sans-serif;color:var(--text);position:relative}
.page{position:absolute;left:63px;top:0;width:1100px;height:2441px;transform:scale(0.4916);transform-origin:0 0;border:1px solid var(--frame);background:var(--white);overflow:hidden}
.abs{position:absolute}

.brand{left:97px;top:30px;color:var(--wine);font-weight:700}
.brand-name{font-size:30px;line-height:1;display:flex;align-items:center;gap:10px}
.brand-name i{display:inline-block;width:14px;height:14px;border-radius:50%;background:var(--wine)}
.brand-tag{font-size:15px;margin-top:8px;color:var(--wine);font-weight:700}

.nav{left:596px;top:42px;display:flex;font-size:15px;color:var(--wine)}
.nav span{padding:0 10px;border-left:1px solid var(--wine);line-height:22px}
.nav span:first-child{border-left:none}

.hero{left:0;top:85px;width:1100px;height:480px;clip-path:polygon(0 56px,100% 0,100% 100%,0 100%);
  background:linear-gradient(135deg,#8c4a4d 0%,#a7686a 40%,#b98486 70%,#9a5a5d 100%)}
.hero-title{left:87px;top:277px;color:var(--white);font-weight:700;font-size:34px;line-height:42px}
.hero-sub{left:88px;top:365px;color:var(--white);font-size:17px;line-height:21px}
.dots{left:553px;top:527px;display:flex;gap:4px}
.dots i{width:10px;height:10px;border-radius:50%;border:1.5px solid var(--white)}
.dots i:first-child{background:var(--white)}

.side-phone{left:953px;top:198px;width:147px;height:43px;background:var(--wine);color:var(--white);font-size:14px;display:flex;align-items:center;gap:10px;padding-left:14px}
.side-mail{left:1048px;top:243px;width:52px;height:41px;background:var(--wine);display:flex;align-items:center;justify-content:center}

.label{font-weight:700;font-size:22px;border-left:3px solid currentColor;padding-left:8px;line-height:22px;padding-top:6px}
.h2{font-weight:700;font-size:46px;line-height:52px}

.about-img{left:78px;top:627px;width:387px;height:257px;background:linear-gradient(120deg,#e6e8ec 0%,#cdd4de 45%,#5a6a86 80%,#2f3b55 100%)}
.about-label{left:541px;top:637px;color:var(--wine)}
.about-h2{left:540px;top:684px;color:var(--wine)}
.about-text{left:544px;top:750px;width:480px;font-size:11px;line-height:17px;color:#222}
.about-text p+p{margin-top:17px}

.services{left:0;top:923px;width:1100px;height:455px;clip-path:polygon(0 55px,100% 0,100% 400px,0 100%);
  background:linear-gradient(160deg,#a36164 0%,#b47c7e 45%,#9d5c5f 100%)}
.services-label{left:100px;top:1047px;color:var(--white)}
.services-h2{left:98px;top:1093px;color:var(--white)}
.svc{color:var(--white);width:320px}
.svc h3{font-size:16px;line-height:20px;font-weight:700}
.svc p{font-size:11px;line-height:14px;margin-top:2px}
.btn-white{display:inline-block;background:var(--white);color:var(--wine);font-weight:700;font-size:11px;padding:0 19px;height:26px;line-height:26px}

.news-label{left:102px;top:1430px;color:var(--wine)}
.news-h2{left:101px;top:1473px;color:var(--wine)}
.news{width:200px}
.news .date{font-size:8px;font-style:italic;color:#333}
.news h3{font-size:16px;line-height:21px;font-weight:700;color:#222;margin-top:8px}
.news p{font-size:11px;line-height:14px;margin-top:6px;color:#222}
.btn-wine{display:inline-block;background:var(--wine);color:var(--white);font-weight:700;font-size:11px;padding:0 10px;height:26px;line-height:26px}
.more{left:101px;top:1763px;height:32px;line-height:32px;padding:0 9px}

.contact{left:0;top:1826px;width:1100px;height:562px;clip-path:polygon(0 57px,100% 0,100% 505px,0 100%);background:var(--wine)}
.contact-label{left:100px;top:1917px;color:var(--white)}
.contact-h2{left:98px;top:1965px;color:var(--white)}
.address{left:98px;top:2073px;color:var(--white);font-size:11px;line-height:14px}
.address strong{font-size:13px;line-height:17px}
.hours{left:349px;top:2070px;color:var(--white);font-size:13px;line-height:17px}
.field{left:637px;width:377px;height:31px;background:var(--white);font-size:8px;font-style:italic;padding:10px 14px;color:#222}
.consent{left:637px;top:2160px;width:377px;display:flex;gap:8px;color:var(--white);font-size:8px;line-height:10px}
.consent i{flex:none;width:9px;height:9px;border:1px solid var(--white);margin-top:1px}
.captcha{left:637px;top:2215px;width:174px;height:45px;background:#f9f9f9;border:1px solid #ccc;font-size:8px;color:#222;display:flex;align-items:center;gap:6px;padding-left:9px}
.captcha i{width:15px;height:15px;border:1.5px solid #bbb;background:#fff;border-radius:2px}
.captcha small{position:absolute;right:8px;bottom:5px;font-size:4px;color:#777}
.send{left:635px;top:2283px;height:30px;line-height:30px;padding:0 21px}

.footer-left{left:98px;top:2400px;font-size:8px;font-style:italic;color:#222}
.footer-right{left:892px;top:2398px;font-size:11px;color:#222}
</style>
</head>
<body>
<div class="page">
  <header>
    <div class="abs brand">
      <div class="brand-name"><i></i>Helene Kivra</div>
      <div class="brand-tag">Steuerberaterin</div>
    </div>
    <nav class="abs nav"><span>Startseite</span><span>Über uns</span><span>Leistungen</span><span>Aktuelles</span><span>Kontakt</span></nav>
  </header>

  <section>
    <div class="abs hero" role="img" aria-label="Foto: Schreibtisch mit Taschenrechner, Tastatur, Kugelschreiber und Finanzbericht in Weinrot getönt"></div>
    <h1 class="abs hero-title">für Selbstständige,<br>Gewerbe und Existenzgründer</h1>
    <p class="abs hero-sub">Buchhaltung | Lohnabrechnungen<br>Jahesabschluss | Steuererklärungen</p>
    <div class="abs dots"><i></i><i></i><i></i></div>
    <div class="abs side-phone">
      <svg width="18" height="18" viewBox="0 0 24 24"><path fill="#fff" d="M6.6 10.8a15.1 15.1 0 0 0 6.6 6.6l2.2-2.2c.3-.3.7-.4 1-.2 1.1.4 2.3.6 3.6.6.6 0 1 .4 1 1V20c0 .6-.4 1-1 1A17 17 0 0 1 3 4c0-.6.4-1 1-1h3.5c.6 0 1 .4 1 1 0 1.3.2 2.5.6 3.6.1.3 0 .7-.2 1z"/></svg>
      0641-555018
    </div>
    <div class="abs side-mail">
      <svg width="20" height="14" viewBox="0 0 20 14"><rect x="0.75" y="0.75" width="18.5" height="12.5" fill="none" stroke="#fff" stroke-width="1.5"/><path d="M1 1l9 7 9-7" fill="none" stroke="#fff" stroke-width="1.5"/></svg>
    </div>
  </section>

  <section>
    <div class="abs about-img" role="img" aria-label="Foto: Beratungsgespräch zwischen Steuerberater und einem jungen Paar"></div>
    <div class="abs label about-label">Über uns</div>
    <h2 class="abs h2 about-h2">Steuerberatung Kivra</h2>
    <div class="abs about-text">
      <p>Meine Kanzlei berät seit deren Gründung im Jahre 2003 Freiberufler, Gewerbetreibende, Kapital­gesellschaften, Personengesellschaften aus den verschiedensten Branchen sowie gemeinnützige Organisationen. Ebenso unterstützen wir gerne Existenzgründer und nebenberuflich Tätige, wie auch Arbeitnehmer, Vermieter und Rentner.</p>
      <p>Mein Team aus erfahrenen Steuerfachangestellten und ich freuen uns, Ihnen kompetent und individuell auf Ihre persönlichen Bedürfnisse abgestimmt, bei Ihren steuerlichen Angelegenheiten zu helfen!</p>
    </div>
  </section>

  <section>
    <div class="abs services" role="img" aria-label="Foto: Taschenrechner und Kugelschreiber auf Zahlenkolonnen in Weinrot getönt"></div>
    <div class="abs label services-label">Leistungen</div>
    <h2 class="abs h2 services-h2">Unsere Leistungen für...</h2>
    <div class="abs svc" style="left:100px;top:1175px">
      <h3>Selbstständige, Gewerbe<br>und Existenzgründer:</h3>
      <p>Buchhaltung | Lohnabrechnungen<br>Jahesabschluss | Steuererklärungen</p>
    </div>
    <div class="abs svc" style="left:428px;top:1195px">
      <h3>Arbeitnehmer:</h3>
      <p>Lohnsteuerjahresausgleich | Veranlagung von Ehegatten<br>und eingetragenen Lebenspartnerschaften</p>
    </div>
    <div class="abs svc" style="left:784px;top:1195px">
      <h3>Sonstige Einkünfte:</h3>
      <p>Rentner und Pensionäre | Vermieter</p>
    </div>
    <span class="abs btn-white" style="left:100px;top:1258px">» mehr</span>
    <span class="abs btn-white" style="left:429px;top:1258px">» mehr</span>
    <span class="abs btn-white" style="left:783px;top:1258px">» mehr</span>
  </section>

  <section>
    <div class="abs label news-label">Aktuelles</div>
    <h2 class="abs h2 news-h2">Steuer-News</h2>
    <article class="abs news" style="left:103px;top:1540px">
      <div class="date">01.03.2019 | Arbeitnehmer</div>
      <h3>Lohnsteuer: Aktuelles zum Dienstwagen</h3>
      <p>Die Privatnutzung von Dienstwagen ist für viele Arbeitnehmer ein attraktiver Lohnbestandteil, obgleich sich dieser Vorteil in aller Regel ...</p>
    </article>
    <article class="abs news" style="left:344px;top:1540px">
      <div class="date">08.10.2018 | Arbeitnehmer</div>
      <h3>Abschreibung bei “Arbeits­wohnung” im Miteigentum eines Ehepaares</h3>
      <p>Die Kosten eines außerhäuslichen Ar­beitszimmers lassen sin in unbes­chränkter Höhe - selbst wenn dort nicht der Tätigkeitsmittelpunkt liegt ...</p>
    </article>
    <article class="abs news" style="left:585px;top:1540px">
      <div class="date">08.10.2018 | Arbeitnehmer</div>
      <h3>Kein Lohnzufluss bei Gehaltsumwandlung für vorzeitigen Ruhesstand</h3>
      <p>Bei der Einrichtung eines Zeitwertkon­tos kann der Arbeitnehmer darauf Teile seines fälligen Arbeitslohns “ansparen”, um diesen dann in einer späteren ...</p>
    </article>
    <article class="abs news" style="left:829px;top:1540px">
      <div class="date">08.10.2018 | Arbeitnehmer</div>
      <h3>Vermietung eines Home­office vom Arbeitnehmer an den Arbeitgeber</h3>
      <p>Wenn ein Arbeitnehmer einen Raum seiner Wohnung bzw. seinen Hauses an den Arbeitgeber vermietet und diesen Raum selbst als Homeoffice nutzt, ...</p>
    </article>
    <span class="abs btn-wine" style="left:101px;top:1677px">» weiterlesen</span>
    <span class="abs btn-wine" style="left:342px;top:1698px">» weiterlesen</span>
    <span class="abs btn-wine" style="left:584px;top:1698px">» weiterlesen</span>
    <span class="abs btn-wine" style="left:827px;top:1698px">» weiterlesen</span>
    <span class="abs btn-wine more">» weitere Artikel</span>
  </section>

  <section>
    <div class="abs contact"></div>
    <div class="abs label contact-label">Kontakt</div>
    <h2 class="abs h2 contact-h2">So erreichen Sie uns</h2>
    <div class="abs address">
      <strong>Steuerberatung Kivra<br>Dipl. Betriebswirtin (FH)<br>Helene Kivra Steuerberaterin</strong><br><br>
      Lindenweg 12<br>35390 Gießen<br><br>
      Telefon: 0641-555018<br>Telefax: 0641-555019<br>E-Mail: info@stbkivra.de
    </div>
    <div class="abs hours">
      <strong>Öffnungszeiten:</strong><br><em>Mo - Do</em><br>08:00 - 16:00 Uhr<br><br>
      <em>Fr</em><br>08:00 - 12:30 Uhr<br><br>
      Termine sind bei Bedarf natürlich<br>auch außerhalb der üblichen<br>Bürozeiten möglich.
    </div>
    <div class="abs field" style="top:1933px">Name*</div>
    <div class="abs field" style="top:1980px">E-Mail*</div>
    <div class="abs field" style="top:2027px">Telefon*</div>
    <div class="abs field" style="top:2075px;height:73px">Nachricht</div>
    <div class="abs consent"><i></i><span>Ich habe die <b>Datenschutzerklärung</b> zur Kenntnis genommen. Ich stimme zu, dass meine Angaben und Daten zur Beantwortung meiner Anfrage elektronisch erhoben und gespeichert werden. Hinweis: Sie können Ihre Einwilligung jederzeit für die Zukunft per E-Mail an info@stbkivra.de widerrufen*</span></div>
    <div class="abs captcha"><i></i>Ich bin kein Roboter.<small>Datenschutz · Nutzung</small></div>
    <span class="abs btn-white send">» senden</span>
  </section>

  <footer>
    <div class="abs footer-left">© 2019 Steuerberatung Kivra</div>
    <div class="abs footer-right">Impressum | Datenschutz</div>
  </footer>
</div>
</body>
</html>
```